Business Card Design for Software Development Company

I am looking for a business card design the incorporates my new logo (attached below).

Key information to include:
Name: Marcus Delvine
Title: CEO
Email: marcus@brightwellcivic.com
Phone: 555-218-4093
Website: www.brightwellcivic.com

NOTE: This design should be easy to edit so that we can order cards for different members of our team.

```html
<!DOCTYPE html>
<html lang="en">
<head>
<meta charset="UTF-8">
<title>BrightwellLabs Business Card</title>
<link rel="stylesheet" href="https://fonts.googleapis.com/css2?family=Montserrat:wght@700&family=Poppins:wght@400;500&family=Archivo+Black&display=swap">
<style>
  :root {
    --page-bg: #161616;
    --card-top: #2c4457;
    --card-bottom: #34536a;
    --pattern-a: #3a566c;
    --pattern-b: #4a6880;
    --ink: #ffffff;
    --accent-teal: #16a892;
    --accent-orange: #ef7a24;
    --accent-red: #c8372b;
  }
  * { box-sizing: border-box; margin: 0; padding: 0; }
  html, body { width: 900px; height: 1200px; overflow: hidden; }
  body {
    background: var(--page-bg);
    position: relative;
    font-family: "Poppins", sans-serif;
    color: var(--ink);
  }
  .card {
    position: absolute;
    width: 630px;
    height: 360px;
    background: linear-gradient(160deg, var(--card-top), var(--card-bottom));
    overflow: hidden;
  }
  .card--front { left: 135px; top: 213px; }
  .card--back  { left: 136px; top: 627px; }

  .front-pattern {
    position: absolute;
    inset: 0;
    background: linear-gradient(160deg, var(--pattern-a), var(--pattern-b));
  }

  .brand {
    position: absolute;
    display: flex;
    align-items: center;
  }
  .brand__dot {
    border-radius: 50%;
    background: var(--accent-orange);
    flex: none;
  }
  .brand__name {
    font-family: "Montserrat", sans-serif;
    font-weight: 700;
    color: var(--ink);
    line-height: 1;
    letter-spacing: -0.5px;
  }
  .brand__tagline {
    position: absolute;
    right: 0;
    font-family: "Montserrat", sans-serif;
    font-weight: 700;
    color: var(--ink);
    white-space: nowrap;
  }

  .card--front .brand { left: 64px; top: 140px; width: 502px; }
  .card--front .brand__dot { width: 44px; height: 44px; margin-right: 14px; }
  .card--front .brand__name { font-size: 52px; }
  .card--front .brand__tagline { bottom: -20px; font-size: 7px; letter-spacing: 0.4px; }

  .card--back .brand { right: 45px; top: 44px; width: 300px; justify-content: flex-end; }
  .card--back .brand__dot { width: 22px; height: 22px; margin-right: 8px; }
  .card--back .brand__name { font-size: 30px; }
  .card--back .brand__tagline { bottom: -11px; font-size: 4.5px; letter-spacing: 0.2px; }

  .contact {
    position: absolute;
    left: 44px;
    top: 190px;
  }
  .contact__name {
    font-family: "Archivo Black", sans-serif;
    font-size: 22px;
    line-height: 1.1;
    background: linear-gradient(180deg, var(--accent-teal) 0 50%, var(--accent-orange) 50% 100%);
    -webkit-background-clip: text;
    background-clip: text;
    color: transparent;
    letter-spacing: 0.3px;
  }
  .contact__title {
    font-size: 13px;
    font-weight: 400;
    margin-top: 2px;
  }
  .contact__rule {
    width: 30px;
    height: 2px;
    margin-top: 4px;
    background: linear-gradient(90deg, var(--accent-teal), var(--accent-orange));
  }
  .contact__list { list-style: none; margin-top: 9px; }
  .contact__item {
    display: flex;
    align-items: center;
    font-size: 14px;
    line-height: 1;
    height: 24px;
    letter-spacing: 0.5px;
  }
  .contact__item--phone { letter-spacing: 3px; }
  .contact__icon { width: 14px; height: 14px; margin-right: 6px; flex: none; }
</style>
</head>
<body>

<section class="card card--front">
  <div class="front-pattern" role="img" aria-label="Repeating faint pattern of the brand symbol across the card"></div>
  <div class="brand">
    <span class="brand__dot"></span>
    <span class="brand__name">BrightwellLabs</span>
    <span class="brand__tagline">A DIVISION OF BRIGHTWELL CIVIC</span>
  </div>
</section>

<section class="card card--back">
  <div class="brand">
    <span class="brand__dot"></span>
    <span class="brand__name">BrightwellLabs</span>
    <span class="brand__tagline">A DIVISION OF BRIGHTWELL CIVIC</span>
  </div>

  <div class="contact">
    <h1 class="contact__name">Marcus Delvine</h1>
    <p class="contact__title">CEO</p>
    <div class="contact__rule"></div>
    <ul class="contact__list">
      <li class="contact__item contact__item--phone">
        <svg class="contact__icon" viewBox="0 0 24 24" aria-hidden="true">
          <path fill="#d9532b" d="M6.6 10.8a15.1 15.1 0 0 0 6.6 6.6l2.2-2.2c.3-.3.7-.4 1-.2 1.1.4 2.3.6 3.6.6.6 0 1 .4 1 1V20c0 .6-.4 1-1 1A17 17 0 0 1 3 4c0-.6.4-1 1-1h3.5c.6 0 1 .4 1 1 0 1.3.2 2.5.6 3.6.1.3 0 .7-.2 1z"/>
        </svg>
        555-218-4093
      </li>
      <li class="contact__item">
        <svg class="contact__icon" viewBox="0 0 24 24" aria-hidden="true">
          <rect x="2" y="5" width="20" height="14" fill="#d9532b"/>
          <path d="M2 5l10 8 10-8" fill="none" stroke="#16a892" stroke-width="2"/>
        </svg>
        marcus@brightwellcivic.com
      </li>
      <li class="contact__item">
        <svg class="contact__icon" viewBox="0 0 24 24" aria-hidden="true">
          <g fill="none" stroke="#d9532b" stroke-width="2">
            <circle cx="12" cy="12" r="9"/>
            <ellipse cx="12" cy="12" rx="4" ry="9"/>
            <path d="M3 12h18M5 7h14M5 17h14"/>
          </g>
        </svg>
        www.brightwellcivic.com
      </li>
    </ul>
  </div>
</section>

</body>
</html>
```